Brook Hollow Patio In-Store Brochure

We sell bbq's, hot tubs, fireplaces, firepits... our company is at www.brookhollowpatio.example . We would like the brochure to highlight some of our best brands (Ember, HeatCraft, TWR, Corvan, DKT & Ventaro grills / Halden BBQ Equipment / Coastal Kindle Works, Brevanto, Stalwick, Parkhurst fireplace / Tidewell Spas (Hot Tubs) / etc. see website!)

Target Market(s)

To give out to people when they come in to the store

Industry/Entity Type

It Company

Requirements
Must have
• An "About Us" section, show the manufacturers/brands that we deal with, have something about the 3 categories we sell to (BBQ/BBQ Equipment/ BBQ Islands.... Hot Tubs by Tidewell Spas..... Fireplaces / Firepits / Fireplace Media ).
Nice to have
• Website, phone, address, email, About Us, Brands that we deal with, etc.

```html
<!DOCTYPE html>
<html lang="en">
<head>
<meta charset="utf-8">
<title>Brook Hollow Patio – In-Store Brochure</title>
<link rel="stylesheet" href="https://fonts.googleapis.com/css2?family=Lato:ital,wght@0,400;0,700;0,900;1,700&display=swap">
<style>
  :root {
    --backdrop: #2b2b2b;
    --paper: #f4f5f8;
    --ink: #3a3c44;
    --ink-soft: #5a5d66;
    --brand-red: #c1121c;
    --brand-red-dark: #8e0c14;
    --tab-grey: #55575d;
    --rule: #6b6d73;
    --photo-sand: #b9a58a;
    --photo-steel: #8e959c;
    --photo-green: #7f8f63;
    --photo-dusk: #5b5a66;
  }
  * { box-sizing: border-box; margin: 0; padding: 0; }
  html, body { width: 1200px; height: 789px; overflow: hidden; }
  body {
    background: var(--backdrop);
    font-family: "Lato", sans-serif;
    color: var(--ink);
    position: relative;
  }
  .spread {
    position: absolute; left: 60px; top: 45px;
    width: 1080px; height: 700px;
    display: flex;
    box-shadow: 0 10px 30px rgba(0,0,0,.5);
  }
  .page {
    position: relative; width: 540px; height: 700px;
    background: var(--paper); overflow: hidden;
  }
  .page--left { border-right: 1px solid #d6d8de; }

  /* About page */
  .about-header { position: absolute; left: 0; top: 0; width: 540px; height: 115px; }
  .about-title {
    position: absolute; left: 34px; top: 26px;
    color: #fff; font-weight: 700; font-style: italic; font-size: 24px;
  }
  .about-body {
    position: absolute; left: 42px; top: 122px; width: 456px;
    font-size: 9.4px; line-height: 1.5; color: var(--ink);
  }
  .about-body p { margin-bottom: 9px; }
  .about-body strong { font-weight: 900; }
  .staff-name { font-size: 13px; font-weight: 700; color: var(--ink); }

  /* Footer */
  .footer-rule {
    position: absolute; left: 0; right: 0; top: 662px; height: 4px;
    background: var(--rule);
  }
  .site-pill {
    position: absolute; top: 651px; height: 26px; width: 200px;
    background: var(--tab-grey); color: #fff; border-radius: 13px;
    font-size: 10px; font-weight: 700;
    display: flex; align-items: center; justify-content: center;
  }
  .page--left .site-pill { left: 300px; }
  .page--right .site-pill { left: 310px; }

  /* Product page */
  .section-rule { position: absolute; height: 1.5px; background: var(--rule); }
  .section-tab {
    position: absolute; left: 28px; height: 30px; width: 150px;
    background: var(--tab-grey); color: #fff;
    border-radius: 0 15px 15px 0;
    font-size: 14px; font-weight: 700;
    display: flex; align-items: center; padding-left: 14px;
  }
  .section-copy {
    position: absolute; font-size: 9.6px; line-height: 1.45;
    color: var(--ink-soft); font-style: italic;
  }
  .photo {
    position: absolute; border: 4px solid #fff;
    box-shadow: 0 1px 4px rgba(0,0,0,.25);
  }
  .photo--sand { background: linear-gradient(160deg, #cdbb9f, var(--photo-sand) 55%, #8f7e66); }
  .photo--steel { background: linear-gradient(160deg, #b7bcc1, var(--photo-steel) 60%, #6c7278); }
  .photo--green { background: linear-gradient(170deg, var(--photo-green), #a7a08c 60%, #c9c3b4); }
  .photo--dusk { background: linear-gradient(170deg, #7e7d8c, var(--photo-dusk) 50%, #3e3b40); }
</style>
</head>
<body>
<main class="spread">

  <!-- About Us page -->
  <section class="page page--left">
    <svg class="about-header" viewBox="0 0 540 115" aria-hidden="true">
      <defs>
        <linearGradient id="redBand" x1="0" x2="1">
          <stop offset="0" stop-color="#9a0d15"/>
          <stop offset="1" stop-color="#d0161f"/>
        </linearGradient>
      </defs>
      <path d="M0 0 H540 V108 C470 70 420 60 340 62 C250 64 180 74 0 76 Z" fill="url(#redBand)"/>
      <path d="M0 76 C180 74 250 64 340 62 C420 60 470 70 540 108 V112 C470 76 420 67 340 68 C250 70 180 80 0 82 Z" fill="var(--brand-red-dark)" opacity=".35"/>
    </svg>
    <h1 class="about-title">About Us</h1>

    <div class="about-body">
      <p>Brook Hollow Patio, Spa &amp; Fireplace was started in 2000 by Martin &amp; Clara Delaney – they were chosen to supply bbq equipment to the Alder Falls community in California and started the business from their home (Martin Delaney Enterprises was the name...). Later, in 2002, they opened up a storefront in Mesa Verde, CA and ran it until 2005. In 2006, their son, Owen Delaney, began to oversee the business and expanded it throughout the Sunridge Valley, offering spas, umbrellas, firepits, fireplaces, accessories – soon the business volume grew larger and because of their buying power, Brook Hollow was able to offer better prices to their clients in the Desert and Harbor County areas.</p>
      <p>Now a family owned corporation, they took over three competing businesses and have expanded its reach to Harbor County. Brook Hollow Patio, Spa &amp; Fireplace has always been both a Distributor AND a Discounter – never Retail – and our new Palm Crest showroom clearly is a working showroom.</p>
      <p>What people enjoy about us is that we have no pricing games, genuine discounts, and a relatively small showroom... that's the way it is <strong>AND WILL ALWAYS BE!</strong></p>
      <p><span class="staff-name">Owen Delaney</span>, Operations Manager, has extensive knowledge in bbq's, heaters, fireplaces, firepits and specialty tubs, working with both manufacturers and dealers for many years. His extensive knowledge base has helped shape many different equipment suppliers, often times being asked to help with the re-design of products. Being a veteran of the industry, Owen knows what it takes to keep a client happy and stays on top of the latest changes and offerings.</p>
      <p><span class="staff-name">Russell Kane</span>, Sales Consultant, has been with Brook Hollow previously, several years ago, and has returned for 'light active duty' a few days per week. Russell is retired and loves to play golf. For the Palm Crest store, he agreed to come out of retirement, so we have him back and he'll be able to help you with most everything in the store.</p>
      <p><span class="staff-name">Nadia Fields</span>, Manager, Nadia has been with us since 2013 in Harbor County, handling the distribution and delivery of the products for our different stores. Her background is with a sales agency for grill vendors, so she understands local contractors and is great with scheduling on the computer. She's great at the scheduling part and you'll be happy too!</p>
      <p>We ARE a direct source for contractors, being able to build specialty products for most anything. We only sell quality – if you want price, then please go elsewhere. Again, it's important to note that we do not subscribe to the foreign-built junk grills, as they tend to be costly to repair and end up costing you more in the long run. Remember: it's your money – Why not get something good for it?</p>
    </div>

    <div class="footer-rule"></div>
    <div class="site-pill">www.brookhollowpatio.example</div>
  </section>

  <!-- Products page -->
  <section class="page page--right">
    <div class="section-rule" style="left:28px; width:484px; top:40px;"></div>
    <h2 class="section-tab" style="top:52px;">BBQ's</h2>
    <p class="section-copy" style="left:40px; top:94px; width:262px;">If You Cook 1 To 2 Times Per Week, We'll Recommend You Stick With The Residential Brands That Offer Performance And Value At A Lower Price. If You Cook More Than 3 Times Per Week, You Definitely Should Consider A Better Piece Of Commercial Equipment Like A HeatCraft Or Ember Pro. And While We Sell Kestrel Pair &amp; Sable, We Are Not Authorized Resellers, But We Do Supply Parts To Our Clients.</p>
    <div class="photo photo--sand" role="img" aria-label="Outdoor BBQ island with stainless grill and tiled stucco base" style="left:320px; top:86px; width:195px; height:150px;"></div>
    <div class="section-rule" style="left:28px; width:290px; top:240px;"></div>
    <div class="photo photo--sand" role="img" aria-label="Grill and cart set up on a patio" style="left:28px; top:252px; width:150px; height:110px;"></div>
    <div class="photo photo--steel" role="img" aria-label="Stainless built-in grill in a stone counter" style="left:186px; top:252px; width:152px; height:110px;"></div>
    <div class="photo photo--steel" role="img" aria-label="Curved BBQ island with bar top" style="left:346px; top:252px; width:170px; height:110px;"></div>

    <h2 class="section-tab" style="top:384px;">BBQ Islands</h2>
    <p class="section-copy" style="left:40px; top:424px; width:245px;">We can help you design your next bbq island or entertainment center. When you buy equipment from us, even if we're not doing the island, we'll help you and share our experience with you. Here are just some photos of islands, but the BEST thing to do is go on the 'Net, type in "BBQ Island Photos", and the 'Net will populate your screen with TONS of ideas!</p>
    <div class="photo photo--green" role="img" aria-label="Stacked stone BBQ island in a garden" style="left:300px; top:402px; width:215px; height:140px;"></div>
    <div class="photo photo--dusk" role="img" aria-label="BBQ island in a backyard at dusk" style="left:28px; top:512px; width:122px; height:112px;"></div>
    <div class="photo photo--dusk" role="img" aria-label="Lit BBQ island with tiled counter at night" style="left:158px; top:532px; width:135px; height:110px;"></div>
    <div class="photo photo--sand" role="img" aria-label="Stucco island with blue-lit grill" style="left:300px; top:552px; width:215px; height:94px;"></div>

    <div class="footer-rule"></div>
    <div class="site-pill">www.brookhollowpatio.example</div>
  </section>

</main>
</body>
</html>
```